Web Design Project for new Anaesthetic Pracitice

We have recently obtained our brand new logo from PixelHarbor and now it's time to move on to our website. We are a new anaesthetic practice that offers state of the art anaesthesia care.

We are after a design that communicates professionalism, along with a modern, forward thinking attitude.

Reason: I would like the chance to see more designs. I have also increased the budget and will be providing a little more guidance on required elements.

I have just increased the budget on this project.  $400 for first place, $100 for second.

Also view the brief for some further guidance to help refine designs

Reason: As our deadline is now almost upon us and we have only just sorted out the issues with our increased budget I thought it only fair to give other designers a chance to see if they wish to participate. As a consolation to you all the project is now guaranteed.

Target Market(s)

Our patients and to a lesser extent the surgeons we work with

Requirements
Must have
• The same clean, sleek modern look that we have in our logo. The logo should feature prominently (examples are uploaded)

Menu system, either vertical or horizontal.
The menu system will include the following:
• Home
• Our People
• Our Hospitals
• Our Charges
• Booking Form
• Patient Information
• Contact Information

If designers think they can find more succinct wording for these categories they are free to try.

Some of these menu entries will in all probability lead to a drop down menu (Or People, Our Hospitals and Patient Information in particular). Consideration to how these menus will look and what they are likely to cover is a must.

If your design is selected you will be asked to produce a PSD for both the main page and for any secondary pages (which will be a development of the main page, with the same basic layout, just with a single lot of content) unless your design is one where all pages on the site look the same (i.e. the main page does not have portions of the other pages or leaders on it)

Design delivered as a layered PSD file so we can have our coders chop and slice it into a CSS website.

Use of the logo as uploaded below

A space reserved for breadcrumbs.

Use of the TrustVane logo, preferably in the footer, but we will accept it at the bottom of a side bar. Examples are included below.

The font in the logo is Sommet. We have the ability to install this as a webfont, feel free to utilise it in the site if you so wish.

Contact information can be either a menu option or in the footer.

Nice to have
• Rotating images (either provide us with dummies or just blank placeholder spaces, we have an in-house professional photographer who will be able to populate any such area)

Either a design with all pages on the site looking the same or with a main home page and a separate, related design for other pages (the full site will have about 30 pages, covering how to get to the office, how to get to the hospitals we work at (with roamly charts), the doctors working for us, our office staff, some information on why we charge what we do, and a range of patient information pages)

Icons for Chatterly and Blipster. We have no need for Vid Nest, Pokk, Snapro or Murmo right now, but if you want to include icons for these, feel free, we can always use them later.

These sort of icons can be placed anywhere but personally I like them in the footer.

A footer menu is not mandatory but if it works better with your design feel free to do so.
Should not have
• Pictures of young doctors in white coats, stethoscopes, cadeucus (staff and serpent), all are clichéd and worn out.

```html
<!DOCTYPE html>
<html lang="en">
<head>
<meta charset="utf-8">
<title>Ridgeway Vale Anaesthetic Specialists</title>
<link href="https://fonts.googleapis.com/css2?family=Play:wght@400;700&family=Arimo:wght@400;700&display=swap" rel="stylesheet">
<style>
:root{
  --red:#e31b23;
  --red-dark:#a50f16;
  --ink:#3a3a3a;
  --text:#444;
  --nav:#111;
  --nav-text:#fff;
  --field-border:#c9c9c9;
  --footer-top:#3b3b3b;
  --footer-bottom:#0e0e0e;
  --grey-icon:#8d8d8d;
}
*{box-sizing:border-box;margin:0;padding:0}
html,body{width:1200px;height:1132px;overflow:hidden}
body{
  position:relative;
  font-family:"Arimo",Arial,sans-serif;
  color:var(--text);
  background:
    radial-gradient(ellipse 700px 160px at 600px 560px,rgba(0,0,0,.07),transparent 70%),
    radial-gradient(ellipse 520px 300px at 80px 380px,rgba(0,0,0,.05),transparent 70%),
    radial-gradient(ellipse 520px 300px at 1130px 380px,rgba(0,0,0,.05),transparent 70%),
    #fff;
}
.topline{position:absolute;left:0;top:0;width:1200px;height:4px;background:var(--red)}

.brand{position:absolute;left:196px;top:32px;display:flex;align-items:center;gap:14px}
.brand-dot{width:62px;height:62px;border-radius:50%;background:var(--red)}
.brand-name{font-family:"Play",sans-serif;font-weight:700;font-size:23px;line-height:27px;color:var(--ink);white-space:nowrap}

.assist{position:absolute;right:176px;top:29px;white-space:nowrap;font-family:"Play",sans-serif;font-size:16px;font-weight:700;color:var(--ink)}
.assist .call{color:var(--red);font-weight:400;margin-left:10px}
.assist .phone{font-weight:400}
.search-top{position:absolute;left:859px;top:66px;width:169px;height:25px;display:flex;border:1px solid #d5d5d5;background:#fff}
.search-top span{flex:1;font-size:9px;color:#888;padding:7px 5px}
.search-top .go{width:28px;background:linear-gradient(#d6d6d6,#aaa);display:flex;align-items:center;justify-content:center}

.nav-shell{position:absolute;left:159px;top:132px;width:881px;height:70px;background:var(--nav)}
.nav{position:absolute;left:159px;top:132px;width:881px;height:52px;display:flex;justify-content:space-between;align-items:center;list-style:none;padding:0 8px 0 12px}
.nav li{flex:none;white-space:nowrap;font-family:"Play",sans-serif;font-weight:700;font-size:13px;color:var(--nav-text);padding:0 6px;height:52px;line-height:52px;border-right:1px solid #2c2c2c}
.nav li:last-child{border-right:none}

.slider{position:absolute;left:159px;top:184px;width:881px;height:337px;background:linear-gradient(var(--red),var(--red-dark));border-top:18px solid var(--nav)}
.slider-photo{position:absolute;left:175px;top:186px;width:850px;height:321px;border:3px solid #333;
  background:linear-gradient(110deg,#2b5b8a 0%,#3a8ab0 20%,#c9d3d8 38%,#e7eaec 60%,#d4dade 85%,#bfc6cb 100%)}
.dots{position:absolute;left:576px;top:512px;display:flex;gap:3px}
.dots i{width:6px;height:6px;background:#ff6b6b;border:1px solid #fff}
.dots i:first-child{background:#ddd}

.tagline{position:absolute;left:0;top:536px;width:1200px;text-align:center;font-family:"Play",sans-serif;font-weight:700;font-size:28px;line-height:32px}
.tagline .lead{color:var(--red)}
.tagline .sub{color:#555}

.section-title{font-family:"Play",sans-serif;font-size:22px;color:var(--red);font-weight:400;white-space:nowrap}
.about{position:absolute;left:161px;top:642px;width:600px}
.about p{font-size:9.5px;line-height:17.5px;margin-top:18px;color:var(--text)}
.about p+p{margin-top:17px}
.agents{position:absolute;left:161px;top:813px;display:grid;grid-template-columns:161px 153px 120px;grid-auto-flow:column;grid-template-rows:repeat(5,17.6px);list-style:none;font-size:9.5px;color:var(--text)}
.agents li::before{content:"▪ ";font-size:7px}

.finder{position:absolute;left:793px;top:642px;width:236px}
.finder .fields{margin-top:14px;display:flex;flex-direction:column;gap:8px;position:relative;z-index:2}
.finder .field{height:20px;border:1px solid var(--field-border);background:#fff;font-size:10px;color:#555;padding:3px 6px}
.finder-plate{position:absolute;left:793px;top:784px;width:251px;height:116px;border-radius:58px;background:radial-gradient(ellipse at 60% 40%,#f04048,var(--red-dark));border:2px solid #ddd}
.finder-btn{position:absolute;left:951px;top:823px;width:77px;height:26px;border-radius:6px;background:var(--red);color:#fff;font-family:"Play",sans-serif;font-size:15px;text-align:center;line-height:26px}

.footer{position:absolute;left:0;top:958px;width:1200px;height:174px;background:linear-gradient(var(--footer-top),var(--footer-bottom) 60%)}
.footer h3{position:absolute;top:33px;font-family:"Play",sans-serif;font-weight:400;font-size:17px;color:#fff;white-space:nowrap}
.events{left:161px}
.newsletter{left:469px}
.findus{left:783px}
.no-events{position:absolute;left:161px;top:64px;font-size:9.5px;color:#eee}
.news-box{position:absolute;left:466px;top:54px;width:247px;height:32px;border-radius:16px;background:#fff}
.news-go{position:absolute;left:682px;top:56px;width:28px;height:28px;border-radius:50%;background:radial-gradient(#888,#333);border:2px solid #ccc;color:#fff;font-family:"Play",sans-serif;font-weight:700;font-size:11px;text-align:center;line-height:24px}
.social{position:absolute;right:174px;top:36px;display:flex;gap:12px}
.social span{display:flex;align-items:center;gap:5px;font-family:"Play",sans-serif;font-size:12px;color:#ddd;white-space:nowrap}
.social span::before{content:"";width:12px;height:12px;border-radius:50%;background:var(--grey-icon)}
.trust-badge{position:absolute;left:159px;top:94px;width:100px;height:58px;border-radius:5px;background:linear-gradient(#fff 70%,var(--red) 70%);border:2px solid #ddd}
.copyright{position:absolute;left:275px;top:134px;font-size:9.5px;color:#eee;white-space:nowrap}
.foot-brand{position:absolute;left:772px;top:96px;display:flex;align-items:center;gap:12px}
.foot-brand .brand-dot{width:46px;height:46px}
.foot-brand .brand-name{color:#fff;font-size:17px;line-height:21px}
</style>
</head>
<body>
<div class="topline"></div>

<header>
  <div class="brand">
    <div class="brand-dot"></div>
    <div class="brand-name">Ridgeway Vale<br>Anaesthetic Specialists</div>
  </div>
  <div class="assist">NEED ASISTANCE? <span class="call">CALL-</span><span class="phone">(155)410-7726</span></div>
  <div class="search-top"><span>Search...</span><div class="go">
    <svg width="12" height="12" viewBox="0 0 12 12"><circle cx="5" cy="5" r="3.5" fill="none" stroke="#fff" stroke-width="1.5"/><line x1="7.5" y1="7.5" x2="11" y2="11" stroke="#fff" stroke-width="1.8"/></svg>
  </div></div>
</header>

<div class="nav-shell"></div>
<ul class="nav">
  <li>HOME</li><li>OUR PEOPLE</li><li>OUR HOSPITALS</li><li>OUR CHARGES</li><li>BOOKING FORM</li><li>PATIENT INFORMATION</li><li>CONTACT</li><li>INFORMATION</li>
</ul>

<div class="slider"></div>
<div class="slider-photo" role="img" aria-label="Close-up photo of an anaesthesia workstation with monitor screen, gauges and flow meters"></div>
<div class="dots"><i></i><i></i><i></i><i></i><i></i></div>

<div class="tagline">
  <div class="lead">Anesthetize up to 5 individual patients simultaneously,</div>
  <div class="sub">with one gas machine</div>
</div>

<section class="about">
  <h2 class="section-title">Ridgeway Vale Anaesthetic Specialist</h2>
  <p>Ridgeway Vale Anesthetic Specialists (RVAS), LLC is an international innovator in the design and manufacture of solutions for longstanding problems in veterinary anesthesia and critical care.</p>
  <p>RVA has developed the Calvane brand of veterinary anesthesia equipment and supplies, including warming blankets, zero dead space (ZDS) breathing masks, veterinary laryngoscopes, and non-heated breathing circuits. Coming soon to the US Market the worlds first HEATED breathing circuits.</p>
</section>
<ul class="agents">
  <li>General anesthetic</li><li>Benzodiazepine</li><li>Etomidate</li><li>DozeKit</li><li>Infiltration analgesia</li>
  <li>Ketamine</li><li>Local anesthetic</li><li>Methohexital</li><li>Midazolam</li><li>Neuraxial blockade</li>
  <li>Thiopentone</li><li>Propofol</li><li>Thiopental</li>
</ul>

<div class="finder-plate"></div>
<section class="finder">
  <h2 class="section-title">Find a Specialist</h2>
  <div class="fields">
    <div class="field">By Name</div>
    <div class="field">Anesthesiology</div>
    <div class="field">By Conditions</div>
    <div class="field">By City</div>
    <div class="field">By Location</div>
  </div>
</section>
<div class="finder-btn">SEARCH</div>

<footer class="footer">
  <h3 class="events">UPCOMING EVENTS</h3>
  <div class="no-events">There are no upcoming events</div>
  <h3 class="newsletter">SIGN UP FOR NEWSLETTER</h3>
  <div class="news-box"></div>
  <div class="news-go">go</div>
  <h3 class="findus">FIND US AT</h3>
  <div class="social"><span>Blipster</span><span>Chatterly</span></div>
  <div class="trust-badge" role="img" aria-label="TrustVane security badge"></div>
  <div class="copyright">Copyright @ 2013 www.ridgewayvale.example. All rights reserved.</div>
  <div class="foot-brand">
    <div class="brand-dot"></div>
    <div class="brand-name">Ridgeway Vale<br>Anaesthetic Specialists</div>
  </div>
</footer>
</body>
</html>
```